School Poster

Design so that these can be placed in classrooms across the school.

Attached is another design we have had done. Use a similar theme.

Consider using themes from https://calderwoodhs.lumorin.edu/

please edit Binder1 doc.

Target Market(s)

Students and teachers

```html
<!DOCTYPE html>
<html lang="en">
<head>
<meta charset="utf-8">
<title>Before You Ask the Teacher – Calderwood High</title>
<link href="https://fonts.googleapis.com/css2?family=Poppins:wght@400;500;600;700;800&family=Bebas+Neue&family=Dancing+Script:wght@600&display=swap" rel="stylesheet">
<style>
  :root{
    --navy:#0b2f6e;
    --navy-deep:#072659;
    --blue:#1f5cc0;
    --sky:#1ea4e6;
    --pale:#dbe7f8;
    --pale-2:#eaf1fb;
    --gold:#f5c431;
    --gold-soft:#fbe7a8;
    --ink:#1b1f2a;
    --red:#e23b3b;
    --red-pale:#f9d8d6;
    --line:#8fb2e3;
    --white:#ffffff;
  }
  *{box-sizing:border-box;margin:0;padding:0}
  html,body{width:1012px;height:1200px;overflow:hidden;background:var(--white)}
  body{font-family:"Poppins",sans-serif;color:var(--ink)}
  .poster{position:relative;width:1012px;height:1200px;border:14px solid var(--navy);background:var(--white);overflow:hidden}
  .abs{position:absolute}

  .blob{position:absolute;border-radius:50%;background:var(--pale-2)}
  .blob--tr{right:-60px;top:-10px;width:260px;height:300px;border-radius:45% 55% 40% 60%}
  .blob--l{left:-40px;top:210px;width:80px;height:90px}
  .blob--bl{left:-70px;top:940px;width:150px;height:200px;background:var(--pale)}
  .blob--gold{right:-30px;top:900px;width:90px;height:100px;background:var(--gold-soft)}
  .dots{position:absolute;display:grid;gap:12px}
  .dots i{display:block;width:3px;height:3px;border-radius:50%;background:var(--line)}

  .brand{left:52px;top:58px;width:110px;display:flex;flex-direction:column;align-items:center;gap:8px}
  .brand__mark{width:52px;height:52px;background:var(--navy)}
  .brand__name{font-weight:700;font-size:17px;color:var(--navy);text-align:center;line-height:1.15}

  .title{left:192px;top:40px}
  .title__small{font-weight:800;font-size:44px;line-height:1;color:var(--navy);letter-spacing:-.5px}
  .title__big{font-weight:800;font-size:62px;line-height:1.02;color:var(--navy);letter-spacing:-1px}
  .title__rule{width:488px;height:3px;background:var(--gold);margin-top:6px}
  .title__sub{font-weight:700;font-size:29px;color:var(--blue);margin-top:2px}

  .header-art{left:690px;top:44px;width:190px;height:150px;border-radius:46% 54% 50% 50%;background:linear-gradient(135deg,var(--ink) 0%,var(--navy) 55%,var(--sky) 100%)}

  .step{position:absolute;top:240px;width:297px;height:300px;border:2px solid var(--line);border-radius:12px;background:var(--white)}
  .step__num{position:absolute;left:50%;top:-24px;transform:translateX(-50%);width:44px;height:44px;border-radius:50%;background:var(--gold);color:var(--navy);font-weight:700;font-size:24px;display:flex;align-items:center;justify-content:center}
  .step__icon{position:absolute;left:50%;top:34px;transform:translateX(-50%);width:84px;height:80px;border-radius:10px;background:linear-gradient(135deg,var(--pale),var(--gold-soft))}
  .step__band{position:absolute;left:0;right:0;top:126px;height:27px;background:var(--navy);color:var(--white);font-weight:700;font-size:18px;text-align:center;line-height:27px}
  .step__band em{font-style:normal;color:var(--gold)}
  .step__lead{position:absolute;left:0;right:0;top:160px;text-align:center;font-weight:600;font-size:12px;padding:0 20px;line-height:1.25}
  .step__cols{position:absolute;left:20px;right:10px;top:186px;display:flex;gap:8px;font-size:12px;line-height:1.3}
  .step__cols ul{list-style:none;flex:1}
  .step__cols ul.wide{flex:1.35}
  .step__cols li{position:relative;padding-left:11px;margin-bottom:4px}
  .step__cols li::before{content:"";position:absolute;left:0;top:6px;width:4px;height:4px;border-radius:50%;background:var(--gold)}
  .step__list{position:absolute;left:22px;right:14px;top:202px;list-style:none;font-size:12px}
  .step__list li{position:relative;padding-left:11px;margin-bottom:5px}
  .step__list li.small{font-size:10px}
  .step__list li::before{content:"";position:absolute;left:0;top:6px;width:4px;height:4px;border-radius:50%;background:var(--gold)}
  .step__close{position:absolute;left:0;right:0;top:272px;text-align:center;font-weight:600;font-size:11px}

  .ai-banner{left:45px;top:566px;width:902px;height:117px;border-radius:60px;background:linear-gradient(90deg,var(--navy-deep),var(--navy) 45%,var(--blue))}
  .ai-banner__art{left:80px;top:528px;width:200px;height:190px;border-radius:50% 50% 46% 46%;background:linear-gradient(160deg,#c9d6ec,#eef2f8)}
  .ai-banner__text{left:392px;top:582px;font-weight:800;line-height:1.05}
  .ai-banner__text .l1{font-size:38px;color:var(--white)}
  .ai-banner__text .l2{font-size:48px;color:var(--gold)}

  .panel{position:absolute;border:2px solid var(--gold);border-radius:8px;background:var(--white)}
  .panel--must{left:62px;top:752px;width:341px;height:230px}
  .panel--approved{left:420px;top:752px;width:520px;height:138px;border-color:var(--pale)}
  .pill{position:absolute;height:37px;border-radius:20px;display:flex;align-items:center;gap:8px;padding:0 14px;font-weight:600;font-size:15.5px;color:var(--navy)}
  .pill--gold{left:82px;top:734px;width:272px;background:#f1c54f}
  .pill--pale{left:430px;top:734px;width:502px;background:var(--pale)}
  .pill--red{left:420px;top:902px;width:273px;background:var(--red-pale)}
  .checks{list-style:none;font-size:14.5px;line-height:1.3}
  .checks li{display:flex;gap:8px;margin-bottom:8px}
  .checks svg{flex:none;margin-top:2px}
  .panel--must .checks{position:absolute;left:24px;top:40px;right:12px}
  .panel--approved .checks{position:absolute;left:24px;top:36px;right:12px}
  .panel--approved .checks li{margin-bottom:3px}

  .ban{position:absolute;width:235px;height:68px;border:1.5px solid var(--red);border-radius:6px;background:var(--white)}
  .ban__x{position:absolute;left:-12px;top:22px;width:24px;height:24px;border-radius:50%;background:var(--red)}
  .ban__icon{position:absolute;left:28px;top:12px;width:42px;height:42px;border-radius:6px;background:linear-gradient(135deg,#bfe6f4,var(--pale))}
  .ban__text{position:absolute;left:86px;top:50%;transform:translateY(-50%);right:10px;font-weight:600;font-size:10.5px;line-height:1.3;color:var(--navy)}

  .values{left:48px;top:1003px;display:flex;align-items:flex-start}
  .value{width:112px;display:flex;flex-direction:column;align-items:center}
  .value__badge{width:68px;height:68px;border-radius:50%;border:3px solid var(--pale);background:var(--line)}
  .value--gold .value__badge{background:var(--gold);border-color:var(--gold-soft)}
  .value__label{font-family:"Bebas Neue",sans-serif;font-size:25px;color:var(--navy);margin-top:14px;line-height:1}
  .value-rule{width:1.5px;height:100px;background:var(--navy);margin-top:5px}

  .footer{left:8px;top:1126px;width:968px;height:46px;background:var(--pale);display:flex;align-items:center;justify-content:center;gap:8px;font-weight:500;font-size:17px;color:var(--navy)}
  .footer__script{font-family:"Dancing Script",cursive;font-size:27px;font-weight:600}
</style>
</head>
<body>
<main class="poster">
  <div class="blob blob--tr"></div>
  <div class="blob blob--l"></div>
  <div class="blob blob--bl"></div>
  <div class="blob blob--gold"></div>
  <div class="dots" style="left:650px;top:22px;grid-template-columns:repeat(4,3px)"><i></i><i></i><i></i><i></i><i></i><i></i><i></i><i></i><i></i><i></i><i></i><i></i></div>
  <div class="dots" style="left:14px;top:438px;grid-template-columns:repeat(2,3px)"><i></i><i></i><i></i><i></i><i></i><i></i><i></i><i></i></div>
  <div class="dots" style="left:945px;top:962px;grid-template-columns:repeat(3,3px)"><i></i><i></i><i></i><i></i><i></i><i></i><i></i><i></i><i></i><i></i><i></i><i></i><i></i><i></i><i></i></div>

  <div class="brand abs">
    <div class="brand__mark"></div>
    <div class="brand__name">Calderwood High</div>
  </div>

  <header class="title abs">
    <div class="title__small">BEFORE YOU ASK</div>
    <div class="title__big">THE TEACHER…</div>
    <div class="title__rule"></div>
    <div class="title__sub">TRY THESE STEPS FIRST!</div>
  </header>

  <div class="header-art abs" role="img" aria-label="Illustration of speech bubbles with a question mark"></div>

  <section class="step" style="left:47px">
    <div class="step__num">1</div>
    <div class="step__icon" role="img" aria-label="Icon of a head with a gear inside"></div>
    <div class="step__band">THINK <em>FIRST</em></div>
    <div class="step__lead">Don’t give up away.</div>
    <div class="step__cols">
      <ul><li>Read the question carefully.</li><li>Try a strategy you’ve used before.</li></ul>
      <ul><li>Indentify what you already know</li><li>Give yourself thinking time.</li></ul>
    </div>
  </section>

  <section class="step" style="left:352px">
    <div class="step__num">2</div>
    <div class="step__icon" role="img" aria-label="Icon of two clasped hands"></div>
    <div class="step__band">CHECK YOUR <em>SUPPORTS</em></div>
    <div class="step__lead">Before asking for help, check</div>
    <div class="step__cols">
      <ul class="wide"><li>Learning goal and success criteria</li><li>Worked examples.</li><li>Class notes.</li><li>Classroom displays.</li></ul>
      <ul><li>StudyHub resources.</li><li>Task sheet and instructions.</li></ul>
    </div>
  </section>

  <section class="step" style="left:656px">
    <div class="step__num">3</div>
    <div class="step__icon" role="img" aria-label="Icon of a student raising a hand with a question bubble"></div>
    <div class="step__band">ASK 3 <em>BEFORE ME</em></div>
    <div class="step__lead">Ask three sources before asking the teacher:</div>
    <ul class="step__list">
      <li>A person (partner or neighbour)</li>
      <li class="small">A resource (worked example, task sheet)</li>
      <li class="small">A place (notes, displays, StudyHub)</li>
    </ul>
    <div class="step__close">Then ask the teacher if you still need help.</div>
  </section>

  <div class="ai-banner abs"></div>
  <div class="ai-banner__art abs" role="img" aria-label="Illustration of a robot rising from a laptop surrounded by chat and mail icons"></div>
  <h2 class="ai-banner__text abs"><span class="l1">USING AI AND OTHER TOOLS</span><br><span class="l2">RESPONSIBLY</span></h2>

  <div class="panel panel--must">
    <ul class="checks">
      <li><svg width="16" height="16" viewBox="0 0 16 16"><circle cx="8" cy="8" r="6.8" fill="none" stroke="var(--navy)" stroke-width="1.5"/><path d="M4.8 8.2l2.2 2.2 4.4-4.6" fill="none" stroke="var(--navy)" stroke-width="1.6"/></svg>Complete your own work</li>
      <li><svg width="16" height="16" viewBox="0 0 16 16"><circle cx="8" cy="8" r="6.8" fill="none" stroke="var(--navy)" stroke-width="1.5"/><path d="M4.8 8.2l2.2 2.2 4.4-4.6" fill="none" stroke="var(--navy)" stroke-width="1.6"/></svg>Demostrate your progress (drafts, notes, planning, revisions)</li>
      <li><svg width="16" height="16" viewBox="0 0 16 16"><circle cx="8" cy="8" r="6.8" fill="none" stroke="var(--navy)" stroke-width="1.5"/><path d="M4.8 8.2l2.2 2.2 4.4-4.6" fill="none" stroke="var(--navy)" stroke-width="1.6"/></svg>Use feedback to imporve your work</li>
      <li><svg width="16" height="16" viewBox="0 0 16 16"><circle cx="8" cy="8" r="6.8" fill="none" stroke="var(--navy)" stroke-width="1.5"/><path d="M4.8 8.2l2.2 2.2 4.4-4.6" fill="none" stroke="var(--navy)" stroke-width="1.6"/></svg>Demostrate your understanding of the ideas in your submission</li>
    </ul>
  </div>
  <div class="pill pill--gold"><svg width="22" height="24" viewBox="0 0 22 24"><path d="M11 1 L20 4 V11 C20 17 16 21 11 23 C6 21 2 17 2 11 V4 Z" fill="var(--navy)"/><path d="M6.5 11.5l3 3 6-6" fill="none" stroke="var(--white)" stroke-width="2"/></svg>What You Must Do:</div>

  <div class="panel panel--approved">
    <ul class="checks">
      <li><svg width="16" height="16" viewBox="0 0 16 16"><circle cx="8" cy="8" r="6.8" fill="none" stroke="var(--navy)" stroke-width="1.5"/><path d="M4.8 8.2l2.2 2.2 4.4-4.6" fill="none" stroke="var(--navy)" stroke-width="1.6"/></svg>Brainstorm ideas</li>
      <li><svg width="16" height="16" viewBox="0 0 16 16"><circle cx="8" cy="8" r="6.8" fill="none" stroke="var(--navy)" stroke-width="1.5"/><path d="M4.8 8.2l2.2 2.2 4.4-4.6" fill="none" stroke="var(--navy)" stroke-width="1.6"/></svg>Check spelling, grammer and clarity</li>
      <li><svg width="16" height="16" viewBox="0 0 16 16"><circle cx="8" cy="8" r="6.8" fill="none" stroke="var(--navy)" stroke-width="1.5"/><path d="M4.8 8.2l2.2 2.2 4.4-4.6" fill="none" stroke="var(--navy)" stroke-width="1.6"/></svg>Read your work aloud using text-to-speech tools</li>
      <li><svg width="16" height="16" viewBox="0 0 16 16"><circle cx="8" cy="8" r="6.8" fill="none" stroke="var(--navy)" stroke-width="1.5"/><path d="M4.8 8.2l2.2 2.2 4.4-4.6" fill="none" stroke="var(--navy)" stroke-width="1.6"/></svg>Help indentify areas for improvement in a draft</li>
    </ul>
  </div>
  <div class="pill pill--pale"><svg width="22" height="24" viewBox="0 0 22 24"><path d="M11 1 L20 4 V11 C20 17 16 21 11 23 C6 21 2 17 2 11 V4 Z" fill="var(--navy)"/><path d="M6.5 11.5l3 3 6-6" fill="none" stroke="var(--white)" stroke-width="2"/></svg>What You Must Do: (when approved by your teacher)</div>

  <div class="pill pill--red"><svg width="22" height="22" viewBox="0 0 22 22"><circle cx="11" cy="11" r="9" fill="none" stroke="var(--red)" stroke-width="2.6"/><path d="M4.8 4.8l12.4 12.4" stroke="var(--red)" stroke-width="2.6"/></svg>What Your Cannot Do:</div>

  <div class="ban" style="left:430px;top:953px">
    <svg class="ban__x" viewBox="0 0 24 24"><path d="M8 8l8 8M16 8l-8 8" stroke="#fff" stroke-width="2.2"/></svg>
    <div class="ban__icon" role="img" aria-label="AI chip icon"></div>
    <div class="ban__text">Submit AI-generated work as yourown</div>
  </div>
  <div class="ban" style="left:691px;top:953px">
    <svg class="ban__x" viewBox="0 0 24 24"><path d="M8 8l8 8M16 8l-8 8" stroke="#fff" stroke-width="2.2"/></svg>
    <div class="ban__icon" role="img" aria-label="Document copy icon"></div>
    <div class="ban__text">Copy and paste AI responses without acknowledging or adapting them</div>
  </div>
  <div class="ban" style="left:430px;top:1030px">
    <svg class="ban__x" viewBox="0 0 24 24"><path d="M8 8l8 8M16 8l-8 8" stroke="#fff" stroke-width="2.2"/></svg>
    <div class="ban__icon" role="img" aria-label="AI document icon"></div>
    <div class="ban__text">Use AI tools to complete the whole task for you</div>
  </div>
  <div class="ban" style="left:691px;top:1030px">
    <svg class="ban__x" viewBox="0 0 24 24"><path d="M8 8l8 8M16 8l-8 8" stroke="#fff" stroke-width="2.2"/></svg>
    <div class="ban__icon" role="img" aria-label="Document upload icon"></div>
    <div class="ban__text">Submit work that does not demostrate your understanding</div>
  </div>

  <div class="values abs">
    <div class="value"><div class="value__badge" role="img" aria-label="Icon of joined hands"></div><div class="value__label">WE BELIEVE</div></div>
    <div class="value-rule"></div>
    <div class="value value--gold"><div class="value__badge" role="img" aria-label="Icon of a figure climbing steps to a trophy"></div><div class="value__label">WE STRIVE</div></div>
    <div class="value-rule"></div>
    <div class="value"><div class="value__badge" role="img" aria-label="Icon of a hand raising a trophy"></div><div class="value__label">WE ACHIEVE</div></div>
  </div>

  <footer class="footer abs">If you didn’t create, develop and understnad it, <span class="footer__script">it isn’t your work.</span></footer>
</main>
</body>
</html>
```